Copperleaf Dukes - Sovereign rings, pendants & custom cultural pieces

I need a website that attracts customers knowing that I am as per detailed below Everyone deserves a special piece of treasure. At Copperleaf Dukes we provide you with unique, high-quality and affordable Sovereign rings, pendants & custom cultural pieces.
Feel free to check my Snapgallery page to get idea's @copperleaf.dukes
I want people to see the Items I have available & know that my prices are very competitive. I want people to be able to Shop/Purchase items via site. I would like to have Copperleaf Dukes Chatterbook, Snapgallery & Swapyard Icon/tabs on site so customers can link a at click of the mouse.

(My Apologies to you all, This is all overwhelming & new to myself & I appreciate your efforts & work detail)
Updates

Apologies, have had family loss to deal with

Still dealing with loss of family member

Still Dealing with Family member passing

As previously, still getting through the loss of a family member

As per previous extensions, re adjusting to life after loss of family member

As per previously still recovering from loss of family member

As previously expressed

Haven’t recovered from family loss

I am still getting life back together

Target Market(s)

Jewellery, Wedding, Gifts, Pacific people, Persons 18 - 65yrs, New Zealand & Australian

Industry/Entity Type

Jewelry

Contact Information for Business Card

Copperleaf Dukes
Rek Tamuno
Chatterbook @copperleafdukes
Snapgallery @copperleaf.dukes
Phone Number 021 04731952
Website www.copperleafdukes.co.nz
Auckland
New Zealand

Number of Pages Required

5+ page

Font styles to use
Sans Serif

Colors
474747
1b1b1b
000000
cfcfcf
fbed22
ffc214
ffffff

Requirements
Must have
• Using Black / Gold Copperleaf Dukes logo with crown, has been attached to Web design.
• Rek Tamuno
• Chatterbook Copperleaf Dukes
• Snapgallery @copperleaf.dukes
• Swapyard Copperleaf Dukes
• Phone Number 021 04731952
• Website www.copperleafdukes.co.nz
Nice to have
• Thinking black card with the Copperleaf Dukes Gold logo
• Lines on back of card for Customer Quoted Prices

```html
<!DOCTYPE html>
<html lang="en">
<head>
<meta charset="utf-8">
<title>Copperleaf Dukes — Sovereign Rings &amp; Pendants</title>
<link rel="stylesheet" href="https://fonts.googleapis.com/css2?family=Cinzel:wght@400;500&family=Raleway:wght@400;500;600&display=swap">
<style>
  :root{
    --gold:#ffc214;
    --gold-soft:#d9a514;
    --black:#000000;
    --ink:#1b1b1b;
    --panel:#262626;
    --mid:#474747;
    --silver:#cfcfcf;
    --white:#ffffff;
    --page:#1e1e1e;
    --footer:#0f0f0f;
  }
  *{margin:0;padding:0;box-sizing:border-box}
  html,body{width:1200px;height:3209px;overflow:hidden}
  body{position:relative;background:var(--page);color:var(--white);font-family:"Raleway",Arial,sans-serif}
  .abs{position:absolute}
  .heading{font-family:"Cinzel",Georgia,serif;color:var(--gold);font-weight:400;font-variant:small-caps;text-align:center;width:1200px;left:0;font-size:34px;letter-spacing:1px}

  /* hero */
  .hero{left:0;top:0;width:1200px;height:706px;background:radial-gradient(ellipse at 40% 40%,#3a3a3a 0%,#242424 55%,#1a1a1a 100%)}
  .hero-photo{left:96px;top:192px;width:460px;height:450px;border-radius:46% 40% 44% 48%;background:radial-gradient(circle at 45% 45%,#6a6a6a 0%,#3e3e3e 50%,#2a2a2a 80%,transparent 82%)}
  .nav a{position:absolute;top:52px;color:var(--silver);font-size:14px;letter-spacing:2px;text-decoration:none;transform:translateX(-50%)}
  .brand{left:601px;top:40px;transform:translateX(-50%);display:flex;flex-direction:column;align-items:center;gap:8px}
  .brand-mark{width:14px;height:14px;background:var(--gold-soft)}
  .brand-name{font-family:"Cinzel",Georgia,serif;font-size:15px;color:var(--gold-soft);letter-spacing:1px;white-space:nowrap}
  .hero-title{top:296px;font-size:41px;letter-spacing:2px}
  .btn{display:flex;align-items:center;justify-content:center;gap:8px;border:2px solid var(--gold);color:var(--gold);font-size:15px;letter-spacing:.5px;text-decoration:none}
  .hero-btn{left:500px;top:426px;width:200px;height:50px}
  .follow-item{position:absolute;left:1163px;writing-mode:vertical-rl;transform:rotate(180deg);color:var(--silver);font-size:12px;letter-spacing:1.5px;white-space:nowrap;line-height:16px}
  .follow-line{left:1171px;top:214px;width:2px;height:140px;background:var(--silver)}
  .dots{background:#2c2c2c}

  /* story */
  .story-text{left:746px;top:836px;width:362px;text-align:right;font-size:17px;line-height:26px;letter-spacing:1.6px;color:var(--white)}
  .story-text p+p{margin-top:26px}

  /* products */
  .tabs span{position:absolute;top:1628px;font-size:15px;letter-spacing:2px;color:var(--white);transform:translateX(-50%)}
  .tabs .active{color:var(--gold)}
  .tab-rule{left:0;top:1661px;width:1200px;height:2px;background:var(--gold-soft)}
  .product{top:1720px;width:192px;height:192px;background:linear-gradient(135deg,#8a8a88 0%,#5c5c5a 55%,#3f3f3d 100%)}
  .product.warm{background:linear-gradient(135deg,#8a8780 0%,#6b5a3c 50%,#3f3d38 100%)}
  .product-shade{background:rgba(20,20,20,.82)}
  .arrow{top:1802px;width:20px;height:28px}

  /* advantages */
  .adv-card{top:2242px;width:218px;height:224px;background:var(--panel);text-align:center}
  .adv-card h3{margin-top:44px;font-size:15px;font-weight:500;letter-spacing:2.5px;color:var(--white)}
  .adv-card .rule{width:70px;height:1px;background:var(--gold);margin:10px auto 0}
  .adv-card p{margin:26px auto 0;width:180px;font-size:11px;line-height:14px;color:var(--silver)}
  .adv-icon{top:2163px;width:104px;height:104px}

  /* arrivals */
  .arrival{top:2672px;width:238px;height:237px;background:linear-gradient(135deg,#8a8780 0%,#6a5840 50%,#3a3835 100%)}
  .arrival.silver{background:linear-gradient(135deg,#9a9a98 0%,#6a6a68 55%,#403f3d 100%)}
  .arrival.dim{background:linear-gradient(135deg,#4a4845 0%,#3a3631 60%,#2a2826 100%)}
  .arrival .name{position:absolute;left:12px;font-size:12px;font-weight:600;letter-spacing:1px;color:var(--white);line-height:16px}
  .arrival .price{position:absolute;left:12px;font-size:15px;font-weight:600;color:var(--white);letter-spacing:1px}
  .arrival .old{position:absolute;left:22px;top:202px;font-size:11px;color:var(--silver);text-decoration:line-through}

  /* footer */
  .footer{left:0;top:3008px;width:1200px;height:201px;background:var(--footer)}
  .foot-head{top:3053px;font-size:14px;letter-spacing:2px;color:var(--gold-soft)}
  .foot-link{font-size:14px;color:var(--silver)}
  .mail-line{left:772px;top:3142px;width:278px;height:1px;background:var(--mid)}
  .mail-ph{left:778px;top:3112px;font-size:14px;color:var(--mid);font-style:italic;letter-spacing:1px}
  .mail-btn{left:1055px;top:3093px;width:51px;height:49px;background:#3a3a3a;display:flex;align-items:center;justify-content:center}
</style>
</head>
<body>

<!-- Hero -->
<section class="abs hero"></section>
<div class="abs hero-photo" role="img" aria-label="Close-up photo of a silver sovereign signet ring on dark stone"></div>

<nav class="nav">
  <a href="#" style="left:192px">SHOP</a>
  <a href="#" style="left:375px">ABOUT</a>
  <a href="#" style="left:806px">PORTFOLIO</a>
  <a href="#" style="left:993px">CONTACT</a>
</nav>
<div class="abs brand"><span class="brand-mark"></span><span class="brand-name">Copperleaf Dukes</span></div>

<h1 class="abs heading hero-title">Everyone Deserves A Special Piece of Treasure</h1>
<a href="#" class="abs btn hero-btn">Shop now
  <svg width="9" height="14" viewBox="0 0 9 14"><path d="M1 1l6 6-6 6" fill="none" stroke="currentColor" stroke-width="2"/></svg></a>

<span class="follow-item" style="top:128px">FOLLOW US</span>
<div class="abs follow-line"></div>
<span class="follow-item" style="top:372px">Chatterbook</span>
<span class="follow-item" style="top:466px">Snapgallery</span>
<span class="follow-item" style="top:580px">Swapyard</span>

<svg class="abs dots" style="left:821px;top:700px" width="379" height="64" aria-hidden="true">
  <g fill="#1a1a1a"><circle cx="47" cy="34" r="15"/><circle cx="118" cy="34" r="15"/><circle cx="186" cy="34" r="15"/><circle cx="257" cy="34" r="15"/><circle cx="326" cy="34" r="15"/></g>
</svg>

<!-- Our Story -->
<h2 class="abs heading" style="top:732px">Our Story</h2>
<svg class="abs" style="left:120px;top:740px" width="600" height="720" role="img" aria-label="Portrait of the founder and photos of sovereign earrings and a gold sovereign ring">
  <polygon points="235,11 457,233 235,455 13,233" fill="#242424" stroke="#c99a14" stroke-width="2"/>
  <polygon points="235,60 408,233 235,406 62,233" fill="url(#portrait)"/>
  <polygon points="475,276 531,332 475,388 419,332" fill="none" stroke="#c99a14" stroke-width="2"/>
  <polygon points="111,387 214,490 111,593 8,490" fill="#3a3835" stroke="#c99a14" stroke-width="2"/>
  <polygon points="396,353 571,528 396,703 221,528" fill="#2a2a2a" stroke="#c99a14" stroke-width="2"/>
  <polygon points="396,385 539,528 396,671 253,528" fill="url(#ringphoto)"/>
  <defs>
    <radialGradient id="portrait" cx="50%" cy="45%" r="55%"><stop offset="0" stop-color="#4a4a4a"/><stop offset="1" stop-color="#1e1e1e"/></radialGradient>
    <radialGradient id="ringphoto" cx="50%" cy="50%" r="55%"><stop offset="0" stop-color="#8a6a40"/><stop offset=".6" stop-color="#5a5650"/><stop offset="1" stop-color="#3a3a38"/></radialGradient>
  </defs>
</svg>
<div class="abs story-text">
  <p>Lorem ipsum dolor sit amet, consectetur adipisicing elit, sed do eiusmod tempor incididunt ut labore et dolore magna aliqua. Ut enim ad minim veniam, quis nostrud exercitation ullamco laboris nisi ut aliquip ex ea commodo consequat.</p>
  <p>Duis aute irure dolor in reprehenderit in voluptate velit esse cillum dolore eu fugiat nulla pariatur. Excepteur sint occaecat cupidatat non proident, sunt in culpa qui officia deserunt mollit anim id est laborum.</p>
</div>

<!-- Our Products -->
<h2 class="abs heading" style="top:1528px">Our Products</h2>
<div class="tabs">
  <span style="left:409px">BRACELET</span>
  <span class="active" style="left:541px">RINGS</span>
  <span style="left:674px">PENDANT</span>
  <span style="left:806px">STUDS</span>
</div>
<div class="abs tab-rule"></div>
<svg class="abs" style="left:529px;top:1661px" width="24" height="14" aria-hidden="true"><path d="M0 1l12 12 12-12" fill="var(--page)" stroke="#d9a514" stroke-width="2"/></svg>

<svg class="abs arrow" style="left:150px" viewBox="0 0 20 28" aria-hidden="true"><path d="M14 4l-9 10 9 10" fill="none" stroke="#d9a514" stroke-width="2"/></svg>
<div class="abs product" style="left:180px" role="img" aria-label="Silver sovereign ring"></div>
<div class="abs product" style="left:396px" role="img" aria-label="Silver sovereign ring"></div>
<div class="abs product-shade" style="left:396px;top:1720px;width:192px;height:192px"></div>
<a href="#" class="abs btn" style="left:436px;top:1790px;width:120px;height:52px;font-size:14px">Shop now
  <svg width="8" height="12" viewBox="0 0 8 12"><path d="M1 1l5 5-5 5" fill="none" stroke="currentColor" stroke-width="1.8"/></svg></a>
<div class="abs product warm" style="left:612px" role="img" aria-label="Gold sovereign signet ring"></div>
<div class="abs product" style="left:828px" role="img" aria-label="Silver medallion ring"></div>
<svg class="abs arrow" style="left:1030px" viewBox="0 0 20 28" aria-hidden="true"><path d="M6 4l9 10-9 10" fill="none" stroke="#d9a514" stroke-width="2"/></svg>

<svg class="abs dots" style="left:0;top:2043px" width="470" height="70" aria-hidden="true">
  <g fill="#1a1a1a"><circle cx="56" cy="36" r="15"/><circle cx="130" cy="36" r="15"/><circle cx="205" cy="36" r="15"/><circle cx="280" cy="36" r="15"/><circle cx="355" cy="36" r="15"/><circle cx="430" cy="36" r="15"/></g>
</svg>

<!-- Advantages -->
<h2 class="abs heading" style="top:2056px">Advantages</h2>

<div class="abs adv-card" style="left:180px"><h3>QUALITY</h3><div class="rule"></div><p>Lorem ipsum dolor sit amet, consectetur adipisicing elit, sed do eiusmod tempor incididunt ut labore et dolore magna aliqua.</p></div>
<div class="abs adv-card" style="left:492px"><h3>UNIQUE</h3><div class="rule"></div><p>Lorem ipsum dolor sit amet, consectetur adipisicing elit, sed do eiusmod tempor incididunt ut labore et dolore magna aliqua.</p></div>
<div class="abs adv-card" style="left:802px"><h3>ELEGANCE</h3><div class="rule"></div><p>Lorem ipsum dolor sit amet, consectetur adipisicing elit, sed do eiusmod tempor incididunt ut labore et dolore magna aliqua.</p></div>

<svg class="abs adv-icon" style="left:237px" viewBox="0 0 104 104" aria-hidden="true">
  <polygon points="52,2 102,52 52,102 2,52" fill="var(--page)" stroke="#ffc214" stroke-width="2"/>
  <path d="M36 44l7-9h18l7 9-16 20z" fill="#ffc214"/>
  <path d="M36 44h32M46 35l6 29M58 35l-6 29" stroke="var(--page)" stroke-width="1.5" fill="none"/>
</svg>
<svg class="abs adv-icon" style="left:549px" viewBox="0 0 104 104" aria-hidden="true">
  <polygon points="52,2 102,52 52,102 2,52" fill="var(--page)" stroke="#ffc214" stroke-width="2"/>
  <g fill="none" stroke="#ffc214" stroke-width="2" stroke-linecap="round">
    <path d="M40 60c-2-6-2-12 1-17 4-7 14-8 19-2"/>
    <path d="M45 64c-3-8-2-15 2-19 3-3 9-3 11 2 2 4 0 9 1 14"/>
    <path d="M51 66c-2-6-1-12 1-15"/>
    <path d="M64 47c2 5 2 11 0 16"/>
  </g>
</svg>
<svg class="abs adv-icon" style="left:859px" viewBox="0 0 104 104" aria-hidden="true">
  <polygon points="52,2 102,52 52,102 2,52" fill="var(--page)" stroke="#ffc214" stroke-width="2"/>
  <path d="M48 34h8l-2 5h-4z" fill="#ffc214"/>
  <path d="M50 40h4l5 22-7 7-7-7z" fill="#ffc214"/>
</svg>

<!-- New Arrival -->
<h2 class="abs heading" style="top:2559px">New Arival</h2>

<div class="abs arrival" style="left:94px" role="img" aria-label="Gold full sovereign coin ring">
  <span class="name" style="top:170px">GOLD FULL SOVEREIGN COIN</span>
  <span class="price" style="top:196px">$2400</span>
</div>
<div class="abs arrival dim" style="left:353px" role="img" aria-label="Full sovereign bracelet with six sovereign coins">
  <span class="name" style="top:12px">FULL SOVEREIGN BRACELET<br>6XSOVEREIGN COINS</span>
  <span class="price" style="top:182px">$7500</span>
  <span class="old">$8000</span>
  <a href="#" class="btn" style="position:absolute;left:108px;top:178px;width:120px;height:48px;font-size:14px">Shop now
    <svg width="8" height="12" viewBox="0 0 8 12"><path d="M1 1l5 5-5 5" fill="none" stroke="currentColor" stroke-width="1.8"/></svg></a>
</div>
<div class="abs arrival" style="left:612px" role="img" aria-label="Gold full sovereign coin ring">
  <span class="name" style="top:170px">GOLD FULL SOVEREIGN COIN</span>
  <span class="price" style="top:196px">$2400</span>
</div>
<div class="abs arrival silver" style="left:868px" role="img" aria-label="Sterling silver medallion coin ring">
  <span class="name" style="top:154px">STERLING SILVER MALO VAI<br>MEDALLION COIN</span>
  <span class="price" style="top:196px">$220</span>
</div>

<!-- Footer -->
<footer class="abs footer"></footer>
<span class="abs foot-head" style="left:165px">FOLLOW US</span>
<span class="abs foot-link" style="left:165px;top:3091px">Chatterbook</span>
<span class="abs foot-link" style="left:165px;top:3118px">Snapgallery</span>
<span class="abs foot-link" style="left:165px;top:3145px">Swapyard</span>
<span class="abs foot-head" style="left:400px">CONTACT US</span>
<span class="abs foot-link" style="left:400px;top:3091px">+ 021 04731952</span>
<span class="abs foot-head" style="left:772px">SUBSCRIBE OUR NEWSLETTER</span>
<span class="abs mail-ph">Enter your e-mail</span>
<div class="abs mail-line"></div>
<div class="abs mail-btn"><svg width="12" height="20" viewBox="0 0 12 20" aria-hidden="true"><path d="M2 2l8 8-8 8" fill="none" stroke="#8a8a8a" stroke-width="2"/></svg></div>

</body>
</html>
```